Web Design for Small Healthcare Startup

Hello,

We are seeking a Website Design for a healthcare company focusing on mobile vaccinations, employee health and wellness services onsite at businesses, and consulting services relating to Healthcare Entities in WA state. Our company’s mission is to “To aid in a healthier workplace”. Brightpath Rovers will provide on-site wellness services to employers that simplify and streamline employee preventative health as well as onsite consulting services to help with compliance of Healthcare Entities.

We are seeking a Website Design for Brightpath Rovers, PLLC. Our company’s mission is to provide mobile health and wellness services to employers onsite at their businesses. These services include mobile vaccinations clinics for employees as well as wellness and health screenings. The company will also offer healtcare compliance consulting services for Healthcare Entities. The company was founded to bring these important healthcare services to businesses and keep employees healthy. Healthy employees are the cornerstone to a great business and we want to help orginazations achieve their goals of having a healthy productive workforce.

We are looking for a moderin website design that will need to be coded. We have attached our current logo design for reference as well as a brief questionare regarding our business for your information (not necessary to include all information). We would like something SEO friendly and easy to navigate.

Thank you!

Brightpath Rovers, PLLC

Target Market(s)

Small Businesses

Industry/Entity Type

Healthcare

Coding

Coded - Design and coding required

Number of Pages Required

1 page

Requirements
Nice to have
• SEO Friendly, Incorporate Logo

```html
<!DOCTYPE html>
<html lang="en">
<head>
<meta charset="utf-8">
<title>Brightpath Rovers, PLLC – On-site Mobile Vaccine Clinics</title>
<meta name="description" content="Brightpath Rovers provides seamless, hassle-free on-site mobile vaccine clinics for employers.">
<link href="https://fonts.googleapis.com/css2?family=Catamaran:wght@500;600;700;800&family=Arimo:wght@400;700&family=Montserrat:wght@500;600&display=swap" rel="stylesheet">
<style>
:root{
  --blue:#0d4ea6;
  --purple:#a2489a;
  --purple-light:#b45aab;
  --ink:#111;
  --text:#333;
  --grey-bg:#f3f3f3;
  --black:#000;
  --white:#fff;
  --grad:linear-gradient(90deg,#1d4aa3,#a2489a);
}
*{margin:0;padding:0;box-sizing:border-box}
html,body{width:1200px;height:3503px;overflow:hidden}
body{position:relative;background:var(--white);font-family:"Arimo",Arial,sans-serif;color:var(--text)}
.abs{position:absolute}
.accent{color:var(--purple)}
.primary{color:var(--blue)}
.rule{position:absolute;width:26px;height:3px;background:var(--blue)}
.btn{position:absolute;display:flex;align-items:center;justify-content:center;border-radius:20px;color:var(--white);font-size:12.5px;text-decoration:none;letter-spacing:.2px}
.btn-purple{background:var(--purple)}
.btn-grad{background:var(--grad)}

.topbar{position:absolute;left:0;top:0;width:1200px;height:5px;background:linear-gradient(90deg,var(--blue) 0 50%,var(--purple) 50% 100%)}
.brand{position:absolute;left:130px;top:27px;display:flex;align-items:center;gap:7px;font-family:"Catamaran",sans-serif;font-weight:700;font-size:15px;color:var(--blue);text-decoration:none;white-space:nowrap}
.brand-dot{width:12px;height:12px;border-radius:50%;background:var(--purple)}
.main-nav{position:absolute;top:33px;left:0;width:1200px;font-size:11.5px;font-weight:700;color:#222}
.main-nav a{position:absolute;color:inherit;text-decoration:none;white-space:nowrap}

.hero-media{position:absolute;left:0;top:75px;width:1200px;height:625px;border-radius:130px 100px 0 130px;
  background:linear-gradient(100deg,#3b3532 0%,#6e6560 28%,#b9b3ae 52%,#8f8b86 70%,#c7c3bf 100%);overflow:hidden}
.hero-media::after{content:"";position:absolute;left:0;bottom:0;width:760px;height:260px;background:radial-gradient(ellipse at 40% 100%,rgba(196,133,48,.8),rgba(196,133,48,0) 70%)}
.hero-kicker{left:131px;top:240px;font-family:"Montserrat",sans-serif;font-weight:600;font-size:14.5px;letter-spacing:1.6px;color:var(--white)}
.hero-title{left:131px;top:272px;white-space:nowrap;font-family:"Catamaran",sans-serif;font-weight:500;font-size:34px;line-height:47px;color:var(--white)}
.hero-sub{left:131px;top:422px;font-size:14.5px;color:var(--white)}
.slider-dots{left:1160px;top:353px}
.slider-dots span{display:block;width:9px;height:9px;border-radius:50%;background:var(--white);margin-bottom:11px}
.slider-dots span:first-child{background:var(--purple-light)}

.section-title{position:absolute;left:0;width:1200px;text-align:center;font-family:"Catamaran",sans-serif;font-weight:700;font-size:35px;color:var(--blue)}
.section-lede{position:absolute;left:0;width:1200px;text-align:center;font-size:12.5px;color:#222}
.feature{position:absolute;top:878px;width:313px;height:307px;border-radius:10px;color:var(--white);text-align:center}
.feature.blue{background:var(--blue)}
.feature.purple{background:var(--purple)}
.feature-icon{position:absolute;left:110px;top:21px;width:92px;height:92px;border-radius:50%;border:2px solid var(--white);display:flex;align-items:center;justify-content:center}
.feature.purple .feature-icon{border:none;background:rgba(255,255,255,.22)}
.feature-title{position:absolute;left:20px;width:273px;top:128px;font-family:"Catamaran",sans-serif;font-weight:700;font-size:15px;line-height:19px}
.feature-line{position:absolute;left:117px;width:78px;height:1px;background:rgba(255,255,255,.8)}
.feature-text{position:absolute;left:18px;width:277px;font-size:10.5px;line-height:22px;text-align:justify;text-align-last:center}
.feature-arrow{position:absolute;left:136px;top:288px;width:40px;height:40px;border-radius:50%;background:var(--grad);border:3px solid var(--white);display:flex;align-items:center;justify-content:center}

.about{position:absolute;left:0;top:1278px;width:1200px;height:513px;background:var(--grey-bg)}
.about-media{position:absolute;left:131px;top:59px;width:397px;height:363px;border-radius:8px;background:linear-gradient(135deg,#d6d9dc,#9aa3ad 50%,#cbbfae);box-shadow:0 8px 18px rgba(0,0,0,.2)}
.split-title{position:absolute;font-family:"Catamaran",sans-serif;font-weight:700;font-size:35px;white-space:nowrap}
.about-lead{position:absolute;left:600px;top:158px;width:480px;font-family:"Catamaran",sans-serif;font-weight:700;font-size:13px;line-height:22px;color:var(--ink)}
.about-text{position:absolute;left:600px;top:214px;width:470px;font-size:11px;line-height:22px;color:#333}

.services{position:absolute;left:0;top:1791px;width:600px;height:539px;background:var(--blue);color:var(--white)}
.services-media{position:absolute;left:600px;top:1791px;width:600px;height:539px;background:linear-gradient(160deg,#c9c6c2,#8c8a88 45%,#bfb3a6)}
.services-lead{position:absolute;left:94px;top:132px;font-family:"Catamaran",sans-serif;font-weight:700;font-size:13px;line-height:22px}
.services-text{position:absolute;left:94px;top:191px;width:470px;font-size:11px;line-height:22px}

.step{position:absolute;top:2578px;width:124px;height:124px;border-radius:50%;background:var(--white);box-shadow:0 2px 10px rgba(0,0,0,.12);display:flex;align-items:center;justify-content:center}
.step::before{content:"";position:absolute;inset:9px;border-radius:50%;border:1.5px dashed var(--purple)}
.step.active{background:var(--grad)}
.step.active::before{border-color:rgba(255,255,255,.7)}
.step-title{position:absolute;top:2722px;width:320px;text-align:center;white-space:nowrap;font-family:"Catamaran",sans-serif;font-weight:700;font-size:15px;line-height:25px;color:var(--ink)}
.step-text{position:absolute;top:2778px;width:250px;text-align:center;font-size:11px;line-height:22px;color:#444}

.dark{position:absolute;left:0;top:2915px;width:1200px;height:588px;background:var(--black);color:var(--white)}
.news-title{position:absolute;left:0;top:82px;width:1200px;text-align:center;font-family:"Catamaran",sans-serif;font-weight:700;font-size:37px}
.news-text{position:absolute;left:0;top:133px;width:1200px;text-align:center;font-size:10.5px}
.news-form{position:absolute;left:222px;top:170px;width:756px;height:70px;border-radius:8px;background:#595959}
.field{position:absolute;top:16px;width:242px;height:39px;background:var(--white);font-size:9px;color:#555;padding:15px 18px}
.news-btn{position:absolute;left:559px;top:15px;width:150px;height:40px;border-radius:20px;background:var(--grad);color:var(--white);font-weight:700;font-size:13px;display:flex;align-items:center;justify-content:center}
.divider{position:absolute;left:126px;width:948px;height:1px;background:#666}
.foot-brand{position:absolute;left:210px;top:345px;display:flex;align-items:center;gap:9px;font-family:"Catamaran",sans-serif;font-weight:700;font-size:23px;color:var(--white);white-space:nowrap}
.foot-brand .brand-dot{width:16px;height:16px;background:var(--white)}
.cards{position:absolute;left:230px;top:393px;display:flex;gap:6px}
.cards span{width:36px;height:21px;border-radius:3px;background:#e9e9e9}
.foot-col{position:absolute;top:318px}
.foot-col h4{font-family:"Catamaran",sans-serif;font-weight:700;font-size:16px;margin-bottom:6px;text-transform:uppercase}
.foot-col ul{list-style:none;font-size:10.5px}
.foot-col li{height:22px;display:flex;align-items:center;gap:9px;white-space:nowrap}
.chev{font-size:9px;width:8px}
.ico{width:9px;height:9px;border-radius:50%;background:var(--white);flex:none}
.copyright{position:absolute;left:0;top:530px;width:1200px;text-align:center;font-size:10.5px}
</style>
</head>
<body>

<header>
  <div class="topbar"></div>
  <a class="brand" href="#home"><span class="brand-dot"></span>Brightpath Rovers</a>
  <nav class="main-nav">
    <a href="#home" style="left:304px">HOME</a>
    <a href="#about" style="left:378px">ABOUT US</a>
    <a href="#services" style="left:477px">OUR SERVICES</a>
    <a href="#schedule" style="left:603px">SCHEDULE TODAY</a>
    <a href="#additional" style="left:746px">ADDITIONAL SERVICE</a>
    <a href="#pricing" style="left:908px">PRICING</a>
    <a href="#contact" style="left:996px">CONTACT US</a>
  </nav>
</header>

<section id="home">
  <div class="hero-media" role="img" aria-label="Hand holding a phone on a video call with a nurse"></div>
  <p class="abs hero-kicker">MAKING THE WORKPLACE A HEALTHIER PLACE.</p>
  <h1 class="abs hero-title">Brightpath Rovers Specializes in<br>Providing Seamless, Hassle-free,<br>on-site Mobile Vaccine Clinics.</h1>
  <p class="abs hero-sub">No crowded waiting rooms, no long lines, no hassle!</p>
  <a class="btn btn-purple" href="#schedule" style="left:132px;top:465px;width:133px;height:39px">GET STARTED</a>
  <div class="abs slider-dots"><span></span><span></span><span></span><span></span></div>
</section>

<section id="welcome">
  <h2 class="section-title" style="top:770px">Welcome To <span class="accent">Brightpath Rovers, PLLC</span></h2>
  <div class="rule" style="left:587px;top:820px"></div>
  <p class="section-lede" style="top:837px">Specializing in workplace employee vaccine clinics. Great service to offer as part of your company's Employee Wellness Package.</p>

  <article class="feature blue" style="left:131px">
    <div class="feature-icon"><svg width="50" height="50" viewBox="0 0 50 50" fill="none" stroke="#fff" stroke-width="2"><path d="M12 38 L8 42 M16 34 l18-18 6 6-18 18z M34 10 l6 6 M37 13 l4-4"/><path d="M20 32 l3 3 M24 28 l3 3 M28 24 l3 3"/></svg></div>
    <h3 class="feature-title" style="top:137px">Offering Flu and Covid vaccinations</h3>
    <div class="feature-line" style="top:159px"></div>
    <p class="feature-text" style="top:168px">Lorem ipsum dolor sit amet, consectetur adipiscing elit, sed do eiusmod tempor incididunt ut labore et dolore magna aliqua. Quis ipsum suspendisse ultrices gravida. Risus commodo viverra maecenas.</p>
    <div class="feature-arrow"><svg width="12" height="12" viewBox="0 0 12 12" fill="none" stroke="#fff" stroke-width="1.6"><path d="M4 1l5 5-5 5"/></svg></div>
  </article>

  <article class="feature purple" style="left:444px">
    <div class="feature-icon"><svg width="48" height="48" viewBox="0 0 48 48" fill="none" stroke="#fff" stroke-width="2"><rect x="6" y="10" width="36" height="32" rx="3"/><path d="M6 18h36M14 6v8M34 6v8"/><rect x="12" y="23" width="6" height="5"/><rect x="21" y="23" width="6" height="5"/><rect x="30" y="23" width="6" height="5"/><rect x="12" y="32" width="6" height="5"/><rect x="21" y="32" width="6" height="5"/><path d="M30 34l2 2 4-4"/></svg></div>
    <h3 class="feature-title">Reserve your on-site mobile vaccine<br>clinic today!</h3>
    <div class="feature-line" style="top:176px"></div>
    <p class="feature-text" style="top:185px">Lorem ipsum dolor sit amet, consectetur adipiscing elit, sed do eiusmod tempor incididunt ut labore et dolore magna aliqua. Quis ipsum suspendisse ultrices gravida. Risus commodo viverra maecenas.</p>
    <div class="feature-arrow"><svg width="12" height="12" viewBox="0 0 12 12" fill="none" stroke="#fff" stroke-width="1.6"><path d="M4 1l5 5-5 5"/></svg></div>
  </article>

  <article class="feature blue" style="left:757px">
    <div class="feature-icon"><svg width="50" height="50" viewBox="0 0 50 50" fill="none" stroke="#fff" stroke-width="2"><rect x="6" y="10" width="34" height="30" rx="3"/><path d="M6 18h34M13 6v8M33 6v8"/><rect x="11" y="23" width="5" height="5"/><rect x="19" y="23" width="5" height="5"/><rect x="27" y="23" width="5" height="5"/><rect x="11" y="31" width="5" height="5"/><rect x="19" y="31" width="5" height="5"/><circle cx="37" cy="36" r="8"/><path d="M33 36l3 3 5-5"/></svg></div>
    <h3 class="feature-title" style="top:137px">Showing available dates/time blocks</h3>
    <div class="feature-line" style="top:159px"></div>
    <p class="feature-text" style="top:168px">Lorem ipsum dolor sit amet, consectetur adipiscing elit, sed do eiusmod tempor incididunt ut labore et dolore magna aliqua. Quis ipsum suspendisse ultrices gravida. Risus commodo viverra maecenas.</p>
    <div class="feature-arrow"><svg width="12" height="12" viewBox="0 0 12 12" fill="none" stroke="#fff" stroke-width="1.6"><path d="M4 1l5 5-5 5"/></svg></div>
  </article>
</section>

<section id="about" class="about">
  <div class="about-media" role="img" aria-label="Nurse with a tablet talking with a senior patient"></div>
  <h2 class="split-title" style="left:600px;top:90px"><span class="primary">About</span> <span class="accent">Brightpath Rovers, PLLC</span></h2>
  <div class="rule" style="left:600px;top:142px"></div>
  <p class="about-lead">To provide on-site wellness services to employers that simplify and streamline employee preventative health.</p>
  <p class="about-text">Pharmacist owned and operated. Brightpath Rovers, PLLC was started by local, Washington state licensed pharmacist with over 15 years experience vaccinating patients. She is a highly skilled immunizer and enjoys interacting with patients while providing this important preventative health services. Her vaccination experience spans from individual patient vaccinations to large clinics during community outbreaks.</p>
  <a class="btn btn-grad" href="#schedule" style="left:600px;top:343px;width:132px;height:39px">CALENDAR</a>
</section>

<section id="services">
  <div class="services">
    <h2 class="split-title" style="left:94px;top:68px;color:#fff">Our Services</h2>
    <div class="rule" style="left:94px;top:116px;background:#fff"></div>
    <p class="services-lead">Brightpath Rovers will come to you!<br>No crowded waiting rooms, no long lines, no hassle!</p>
    <p class="services-text">Hassle-free, streamlining the vaccination process … provide this on-site service as part of your employee wellness package<br>Serving employers who want to increase the health and Wellness of their workplace vaccines including seasonal flu, COVID, Pneumonia<br>Ensure your employees and their families remain healthy this flu season. Host a flu shot clinic on site to help your employees get vaccinated. Provide this service as part of your employee Wellness benefits package.<br>Brightpath Rovers specializes in providing seamless, hassle-free vaccine clinics.<br>Don't wait for your employees to get their vaccines at their next doctor's appointment or visit to the pharmacy.</p>
    <a class="btn btn-purple" href="#additional" style="left:94px;top:425px;width:132px;height:39px">LEARN MORE</a>
  </div>
  <div class="services-media" role="img" aria-label="Person on a laptop video call with a doctor"></div>
</section>

<section id="pricing">
  <h2 class="section-title" style="top:2416px">Our <span class="accent">Pricing Plan</span></h2>
  <div class="rule" style="left:587px;top:2466px"></div>
  <p class="section-lede" style="top:2489px;color:var(--purple);font-family:'Catamaran',sans-serif;font-weight:700;font-size:13px">Hassle-free, streamlining the vaccination process</p>
  <p class="section-lede" style="top:2518px;font-size:11px">Price quote is simple! No hidden travel/mileage calculations, no hidden hourly fees.</p>

  <svg class="abs" style="left:150px;top:2600px" width="690" height="80" viewBox="0 0 690 80" fill="none" stroke="#333" stroke-width="1.2" stroke-dasharray="5 4">
    <path d="M0 52 C30 40 50 70 40 48 C30 28 60 40 90 52"/>
    <path d="M222 48 C240 60 260 30 240 36 C226 42 262 60 290 46 C320 30 350 40 372 40"/>
    <path d="M516 38 C540 58 560 30 544 34 C528 40 560 62 590 48 C620 34 640 60 630 48 C620 36 660 36 680 40"/>
  </svg>

  <div class="step" style="left:244px"><svg width="60" height="60" viewBox="0 0 60 60" fill="none" stroke="#7a4aa6" stroke-width="2"><circle cx="30" cy="30" r="10"/><path d="M30 12v6M30 42v6M12 30h6M42 30h6M17 17l4 4M39 39l4 4M43 17l-4 4M17 43l4-4"/><path d="M12 50l14-14M22 44l-4-4" stroke="#1d4aa3"/></svg></div>
  <div class="step active" style="left:536px"><svg width="64" height="64" viewBox="0 0 64 64" fill="none" stroke="#fff" stroke-width="2.4"><rect x="8" y="12" width="40" height="36" rx="3"/><path d="M8 21h40M17 7v9M39 7v9"/><path d="M14 27h6M24 27h6M34 27h6M14 35h6M24 35h6M14 42h6"/><circle cx="46" cy="44" r="10"/><path d="M46 38v6l4 2"/></svg></div>
  <div class="step" style="left:828px"><svg width="56" height="56" viewBox="0 0 56 56" fill="none" stroke="#5a4aa6" stroke-width="2"><circle cx="28" cy="16" r="8"/><path d="M14 48V34c0-6 6-10 14-10s14 4 14 10v14z"/><path d="M28 24v24M24 26l4 6 4-6"/></svg></div>

  <h3 class="step-title" style="left:146px">Submit Vaccine Clinic Needs<br>Questionnaire.</h3>
  <h3 class="step-title" style="left:438px">Brightpath Rovers, Pllc Will Contact You to<br>Schedule on-site Vaccine Clinic.</h3>
  <h3 class="step-title" style="left:730px">Prepare Your Employees for<br>Vaccine Clinic Day.</h3>
  <p class="step-text" style="left:181px">Lorem ipsum dolor sit amet, consectetur adipiscing elit, sed do eiusmod tempor incididunt ut labore et dolore magna aliqua.</p>
  <p class="step-text" style="left:473px">Lorem ipsum dolor sit amet, consectetur adipiscing elit, sed do eiusmod tempor incididunt ut labore et dolore magna aliqua.</p>
  <p class="step-text" style="left:765px">Lorem ipsum dolor sit amet, consectetur adipiscing elit, sed do eiusmod tempor incididunt ut labore et dolore magna aliqua.</p>
</section>

<footer id="contact" class="dark">
  <h2 class="news-title">Subscribe To Our Newsletter</h2>
  <p class="news-text">Lorem ipsum dolor sit amet, consectetur adipiscing elit sed do eiusmod tempor incididunt ut labore et dolore magna aliqua Ut enim ad minim.</p>
  <form class="news-form">
    <div class="field" style="left:48px">Full Name</div>
    <div class="field" style="left:300px">Email Address</div>
    <div class="news-btn">SUBSCRIBE</div>
  </form>
  <div class="divider" style="top:275px"></div>

  <div class="foot-brand"><span class="brand-dot"></span>Brightpath Rovers</div>
  <div class="cards"><span></span><span></span><span></span><span></span></div>

  <div class="foot-col" style="left:509px">
    <h4>Quick Links</h4>
    <ul>
      <li><span class="chev">»</span>Home</li><li><span class="chev">»</span>About Us</li><li><span class="chev">»</span>Our Services</li><li><span class="chev">»</span>Schedule Today</li><li><span class="chev">»</span>Additional Service</li><li><span class="chev">»</span>Pricing</li><li><span class="chev">»</span>Contact Us</li>
    </ul>
  </div>
  <div class="foot-col" style="left:688px">
    <h4>Follow Us</h4>
    <ul>
      <li><span class="ico"></span>Community</li><li><span class="ico"></span>Gallery</li><li><span class="ico"></span>Updates</li><li><span class="ico"></span>Network</li><li><span class="ico"></span>Videos</li>
    </ul>
  </div>
  <div class="foot-col" style="left:848px">
    <h4>Contact Us</h4>
    <ul>
      <li style="height:44px;align-items:flex-start;line-height:22px"><svg width="9" height="12" viewBox="0 0 9 12" style="margin-top:5px;flex:none"><path d="M4.5 0A4.5 4.5 0 0 0 0 4.5C0 8 4.5 12 4.5 12S9 8 9 4.5A4.5 4.5 0 0 0 4.5 0z" fill="#fff"/><circle cx="4.5" cy="4.5" r="1.6" fill="#000"/></svg><span>123 Lorem ipsum dolor sit amet<br>consectetur adipiscing.</span></li>
      <li style="height:40px"><svg width="10" height="10" viewBox="0 0 10 10" style="flex:none"><rect width="10" height="10" rx="2" fill="#fff"/><path d="M3 2.5l1 2-1 1c.6 1 1 1.4 2 2l1-1 2 1-.5 1.5C5 9 1 5 1.5 3z" fill="#000"/></svg>555-014-2287</li>
      <li><svg width="10" height="8" viewBox="0 0 10 8" style="flex:none"><rect width="10" height="8" fill="#fff"/><path d="M0 0l5 4 5-4" stroke="#000" fill="none"/></svg>hello@brightpathrovers.example</li>
    </ul>
  </div>

  <div class="divider" style="top:510px"></div>
  <p class="copyright">© copyrights 2022 Brightpath Rovers, PLLC &nbsp; | &nbsp;&nbsp; All rights reserved.</p>
</footer>

</body>
</html>
```